Letterhead, stationery and email signature for construction business

I need the letterhead, stationery and email signature designs for a construction business. I want them to have a corporate feel to them.

I've attached the logo for reference.

```html
<!DOCTYPE html>
<html lang="en">
<head>
<meta charset="utf-8">
<title>Halden Builders – Stationery</title>
<link href="https://fonts.googleapis.com/css2?family=Arimo:wght@400;700&family=Rubik:wght@500&display=swap" rel="stylesheet">
<style>
  :root {
    --brand-blue: #2f56a6;
    --brand-slate: #4d4f5a;
    --text-grey: #555559;
    --backdrop: #dedede;
    --paper: #ffffff;
  }
  * { box-sizing: border-box; margin: 0; padding: 0; }
  html, body { width: 891px; height: 1200px; overflow: hidden; }
  body {
    background: var(--backdrop);
    font-family: "Arimo", Arial, sans-serif;
    color: var(--text-grey);
    position: relative;
  }
  .sheet, .card { position: absolute; background: var(--paper); overflow: hidden; }
  .sheet { left: 109px; top: 69px; width: 538px; height: 762px; }
  .card { left: 105px; top: 908px; width: 546px; height: 183px; }
  .corner { position: absolute; left: 0; top: 0; }
  .brand { position: absolute; display: flex; align-items: center; }
  .brand-mark { background: var(--brand-slate); flex: none; }
  .brand-name { color: var(--brand-blue); font-weight: 700; letter-spacing: 0.3px; white-space: nowrap; }
  .sheet .brand { left: 49px; top: 47px; gap: 7px; }
  .sheet .brand-mark { width: 34px; height: 34px; }
  .sheet .brand-name { font-size: 14px; }
  .card .brand { left: 57px; top: 60px; gap: 9px; }
  .card .brand-mark { width: 42px; height: 42px; }
  .card .brand-name { font-size: 16px; }

  .header-contact { position: absolute; left: 305px; top: 46px; display: flex; font-size: 9.7px; line-height: 14px; }
  .header-address { text-align: right; padding-right: 8px; border-right: 1px solid var(--text-grey); }
  .contact-list { list-style: none; padding-left: 8px; }
  .contact-list li { display: flex; align-items: center; gap: 5px; white-space: nowrap; }
  .icon { width: 8px; height: 8px; flex: none; }

  .letter { position: absolute; left: 48px; top: 234px; width: 442px; }
  .salutation { font-family: "Rubik", sans-serif; font-weight: 500; font-size: 12px; margin-bottom: 16px; }
  .letter p { font-size: 9px; line-height: 11px; margin-bottom: 9.5px; }
  .closing { position: absolute; left: 49px; top: 498px; font-family: "Rubik", sans-serif; font-weight: 500; font-size: 7px; color: var(--text-grey); }
  .signature { position: absolute; left: 49px; top: 530px; width: 88px; height: 27px;
    background: linear-gradient(90deg, #e9e9ec, #d9dade); border-radius: 3px; }

  .card-divider { position: absolute; left: 306px; top: 34px; width: 1px; height: 92px; background: var(--text-grey); }
  .card-person { position: absolute; left: 326px; top: 30px; }
  .person-name { color: var(--brand-blue); font-weight: 700; font-size: 18px; line-height: 20px; }
  .person-role { font-size: 13px; line-height: 16px; }
  .card .contact-list { position: absolute; left: 326px; top: 74px; padding: 0; font-size: 13px; line-height: 19px; }
  .card .contact-list li { gap: 7px; }
  .card .icon { width: 10px; height: 10px; }
  .card-rule { position: absolute; left: 24px; top: 144px; width: 498px; height: 1px; background: var(--brand-slate); }
  .card-address { position: absolute; left: 0; top: 154px; width: 546px; text-align: center; font-size: 13px; }
</style>
</head>
<body>

<svg width="0" height="0" style="position:absolute">
  <defs>
    <symbol id="ico-phone" viewBox="0 0 10 10"><path d="M2 1 L3.6 1 L4.2 3 L3.2 3.8 Q4 5.6 6.2 6.8 L7 5.8 L9 6.4 L9 8 Q8.6 9 7.6 9 Q1 8.4 1 2.4 Q1 1.4 2 1 Z" fill="none" stroke="#2f56a6" stroke-width="1"/></symbol>
    <symbol id="ico-mail" viewBox="0 0 10 10"><rect x="0.8" y="2" width="8.4" height="6" fill="none" stroke="#2f56a6" stroke-width="1"/><path d="M0.8 2 L5 5.4 L9.2 2" fill="none" stroke="#2f56a6" stroke-width="1"/></symbol>
    <symbol id="ico-web" viewBox="0 0 10 10"><g fill="none" stroke="#2f56a6" stroke-width="0.8"><circle cx="5" cy="5" r="4.2"/><ellipse cx="5" cy="5" rx="1.8" ry="4.2"/><path d="M0.8 5 H9.2 M1.6 3 H8.4 M1.6 7 H8.4"/></g></symbol>
  </defs>
</svg>

<section class="sheet" aria-label="Letterhead">
  <svg class="corner" width="200" height="135" viewBox="0 0 200 135">
    <polygon points="0,0 16,0 43,33 43,91 0,132" fill="var(--brand-blue)"/>
    <polygon points="23,0 138,0 96,40 49,40" fill="var(--brand-slate)"/>
  </svg>
  <div class="brand"><span class="brand-mark"></span><span class="brand-name">HALDEN BUILDERS</span></div>

  <div class="header-contact">
    <div class="header-address">Your Address<br>City<br>State, Zip 0000</div>
    <ul class="contact-list">
      <li><svg class="icon"><use href="#ico-phone"/></svg>123-456-2100</li>
      <li><svg class="icon"><use href="#ico-mail"/></svg>youremail@mailbox.com</li>
      <li><svg class="icon"><use href="#ico-web"/></svg>www.yourwebsite.com</li>
    </ul>
  </div>

  <div class="letter">
    <h1 class="salutation">Dear Mr. Marsh,</h1>
    <p>Lorem ipsum dolor sit amet, consectetuer adipiscing elit, sed diam nonmmy nibh euismod tincidunt ut laor eet dolore magna aliquam erat volutpat. Ut wisi enim ad minim veniam, quis nostrud exerci tationmcorper suscipit lobortis nisl ut aliquip ex ea commodo consequat. Duis autem vel eum iriure dolor in hendrerit in vulputate velit esse molestie consequat, vel illum dolore eu feugiat</p>
    <p>Rorem ipsum dolor sit amet, consectetuer adipiscing elit, sed diam nonmmy nibh euismod tincidunt ut laor eet dolore magna aliquam erat volutpat. Ut wisi enim ad minim veniam, quis nostrud exerci tationmcorper suscipit lobortis nisl ut aliquip ex ea commodo consequat. Duis autem vel eum iriure dolor in hendrerit in vulputate velit esse molest</p>
    <p>Dorem ipsum dolor sit amet, consectetuer adipiscing elit, sed diam nonmmy nibh euismod tincidunt ut laor eet dolore magna aliquam erat volutpat. Ut wisi enim ad minim veniam, quis nostrud exerci tationmcorper suscipit lobortis nisl ut aliquip ex ea commodo consequat. Duis autem vel eum iriure dolor in hendrerit in suscipit lobortis nisl ut aliquip ex ea commodo consequat. Duis autem vel eum iriure dolor in hendrerit in vulputate velit esse molestie consequat, vel illum</p>
    <p>Sorem ipsum dolor sit amet, consectetuer adipiscing elit, sed diam nonmmy nibh euismod tincidunt ut laor eet dolore magna aliquam erat volutpat. Ut wisi enim ad minim veniam, quis nostrud exerci tationmcorper suscipit lobortis nisl ut aliquip ex ea commodo consequat. Duis autem vel eum iriure dolor in</p>
  </div>
  <div class="closing">Sincerely,</div>
  <div class="signature" role="img" aria-label="Handwritten signature"></div>
</section>

<section class="card" aria-label="Business card">
  <svg class="corner" width="200" height="160" viewBox="0 0 200 160">
    <polygon points="0,0 19,0 51,37 51,109 0,155" fill="var(--brand-blue)"/>
    <polygon points="28,0 163,0 114,47 52,47" fill="var(--brand-slate)"/>
  </svg>
  <div class="brand"><span class="brand-mark"></span><span class="brand-name">HALDEN BUILDERS</span></div>
  <div class="card-divider"></div>
  <div class="card-person">
    <div class="person-name">DANIEL MARSH</div>
    <div class="person-role">Manager</div>
  </div>
  <ul class="contact-list">
    <li><svg class="icon"><use href="#ico-phone"/></svg>123-456-2100</li>
    <li><svg class="icon"><use href="#ico-mail"/></svg>youremail@mailbox.com</li>
    <li><svg class="icon"><use href="#ico-web"/></svg>www.yourwebsite.com</li>
  </ul>
  <div class="card-rule"></div>
  <div class="card-address">Your Address, City, State, Zip 0000</div>
</section>

</body>
</html>
```